Pet business needs a business card

Pet shop needs a business card. Like dark background and and debased look.

Meadowpaws
Lindenweg 47
B - 3280 Velmor
Belgium

www.meadowpaws-example.com
mail@meadowpaws-example.com
Phone +32478610927

I will ad a tagline shortly.

Industry/Entity Type

Shop

Font styles to use
Sans Serif

Requirements
Must have
• Must be possible to print the card debased. See example image.

```html
<!DOCTYPE html>
<html lang="en">
<head>
<meta charset="utf-8">
<title>Meadowpaws business card</title>
<link rel="stylesheet" href="https://fonts.googleapis.com/css2?family=Source+Sans+3:wght@400;600;700&display=swap">
<style>
  :root {
    --stage-light: #5a5a5a;
    --stage-dark: #1f1f1f;
    --card-dark: #2d313a;
    --accent: #f7981f;
    --paper: #ffffff;
    --ink: #3a3a3a;
  }
  * { margin: 0; padding: 0; box-sizing: border-box; }
  html, body { width: 1200px; height: 999px; overflow: hidden; }
  body {
    position: relative;
    font-family: "Source Sans 3", Arial, sans-serif;
    background: radial-gradient(ellipse at 50% 40%, var(--stage-light) 0%, #454545 50%, var(--stage-dark) 100%);
  }
  .card {
    position: absolute;
    width: 753px;
    height: 431px;
    background: var(--paper);
    overflow: hidden;
  }
  .card--front { left: 134px; top: 68px; }
  .card--back { left: 322px; top: 522px; }
  .card__header {
    position: absolute;
    left: 0; top: 0; width: 100%;
    background: var(--card-dark);
  }
  .card--front .card__header { height: 208px; }
  .card--back .card__header { height: 304px; }
  .card__band {
    position: absolute;
    left: 0; width: 100%; height: 11px;
    background: var(--accent);
  }
  .card--front .card__band { top: 208px; }
  .card--back .card__band { top: 304px; }
  .card__pointer {
    position: absolute;
    width: 0; height: 0;
    border-left: 19px solid transparent;
    border-right: 19px solid transparent;
    border-top: 19px solid var(--accent);
  }
  .card--front .card__pointer { left: 30px; top: 218px; }
  .card--back .card__pointer { left: 30px; top: 314px; }
  .brand-name {
    position: absolute;
    color: var(--accent);
    font-weight: 700;
    letter-spacing: 0.5px;
    line-height: 1;
  }
  .card--front .brand-name { left: 30px; top: 118px; font-size: 46px; }
  .card--back .brand-name { left: 34px; top: 172px; font-size: 84px; }
  .details {
    position: absolute;
    left: 34px; top: 270px;
    color: var(--ink);
  }
  .details__name { font-size: 21px; font-weight: 700; line-height: 26px; }
  .details__address { font-size: 18px; line-height: 24px; margin-bottom: 18px; }
  .contact {
    display: flex;
    align-items: center;
    font-size: 18px;
    line-height: 24px;
    margin-bottom: 12px;
  }
  .contact__icon { width: 24px; height: 24px; margin-right: 12px; flex: none; }
  .website {
    position: absolute;
    left: 34px; top: 372px;
    margin: 0;
  }
</style>
</head>
<body>
  <section class="card card--front">
    <div class="card__header"></div>
    <p class="brand-name">Meadowpaws</p>
    <div class="card__band"></div>
    <div class="card__pointer"></div>
    <div class="details">
      <p class="details__name">Meadowpaws</p>
      <p class="details__address">Lindenweg 47, B - 3280 Velmor, Belgium</p>
      <p class="contact">
        <svg class="contact__icon" viewBox="0 0 24 24" aria-hidden="true">
          <rect x="1" y="1" width="22" height="22" rx="4" fill="#f7981f"/>
          <path d="M9 5c-1.5 1-2.5 3-1.5 6.5s3.5 6.5 6.5 7.5c1.5.4 2.5-.5 3-1.5l-2.5-2-1.5 1c-1.5-.8-3-3-3.5-4.5l1.3-1.2L9 5z" fill="#fff"/>
        </svg>
        +32478610927
      </p>
      <p class="contact">
        <svg class="contact__icon" viewBox="0 0 24 24" aria-hidden="true">
          <path d="M1 9l11-7 11 7v13H1z" fill="#f7981f"/>
          <path d="M1 9l11 7 11-7" fill="none" stroke="#fff" stroke-width="1.5"/>
        </svg>
        mail@meadowpaws-example.com
      </p>
    </div>
  </section>

  <section class="card card--back">
    <div class="card__header"></div>
    <p class="brand-name">Meadowpaws</p>
    <div class="card__band"></div>
    <div class="card__pointer"></div>
    <p class="contact website" style="color: var(--ink);">
      <svg class="contact__icon" viewBox="0 0 24 24" aria-hidden="true">
        <g fill="none" stroke="#f7981f" stroke-width="1.6">
          <circle cx="12" cy="12" r="10"/>
          <ellipse cx="12" cy="12" rx="4.5" ry="10"/>
          <path d="M2 12h20M4 6.5h16M4 17.5h16"/>
        </g>
      </svg>
      www.meadowpaws-example.com
    </p>
  </section>
</body>
</html>
```